■依頼目的 / 概要
電子書籍Lumora本を出版いたしますので、
表紙デザイン作成をお願いいたします。

■納品物
下記での納品をお願い致します。

JPEG形式 及び PSD形式
横1600ピクセル x 縦2560ピクセル

■本の内容

<本のタイトル>
雑貨長者の資金調達術 〜開業ローン篇〜

<サブタイトル>
会社をつくる お金を借りる 原資ができる

<キャッチコピー>
貯金してから起業なんて絶対ダメ!

<著者名>
早川蒼一

■デザイン要望
・本のタイトル / キャッチコピー / 著者名の反映をお願いします

デザインイメージ

・人物や風景の画像を背景にしていただき、
その上にタイトル等コピーを記載

・シンプルな背景にタイトル等のコピーを記載

・資産形成に関する指南書。
その第一歩である新規創業融資に
焦点を当てた内容になっていますが、
お金に関することだけではなく、
人間関係や人生設計にまで
踏み込んだ内容になっています。

・楽して稼ぐといったレベルの低いイメージをもたせるような
デザインにはしたくありません。

<表現したいイメージなど>
・高級感
・かっこいい
・信頼感

<表現したくないイメージ>
・安っぽい
・嘘くさい
・大衆的

<利用画像について>
画像素材を使用される場合には、
商用利用可の素材をお願いします。

■その他
デザインを考えるのに必要な情報が他にございましたら、
お答えしますので、遠慮なくご連絡ください。

数あるご提案の中で、もっとも世界観を表現していただいているものを当選に選ばせていただきました。

この度は、たくさんのご提案ありがとうございました。
レベルの高いご提案が多く、非常に良いデザインを得ることができました。
今回、ご縁がなかったデザイナー様。また次回、ご提案いただければ幸いです。
ありがとうございました!

```html
<!DOCTYPE html>
<html lang="ja">
<head>
<meta charset="utf-8">
<title>雑貨長者の資金調達術 〜開業ローン篇〜</title>
<link href="https://fonts.googleapis.com/css2?family=Noto+Sans+JP:wght@700;900&family=Noto+Serif+JP:wght@700;900&display=swap" rel="stylesheet">
<style>
  :root {
    --paper: #f4f4f3;
    --paper-edge: #dcdcda;
    --ink: #141414;
    --red: #e0121b;
    --rule: #2a2a2a;
  }
  html, body { margin: 0; padding: 0; overflow: hidden; }
  .cover {
    position: relative;
    width: 750px; height: 1200px;
    overflow: hidden;
    background: radial-gradient(ellipse at 50% 45%, #ffffff 0%, var(--paper) 60%, var(--paper-edge) 100%);
    font-family: "Noto Serif JP", serif;
    color: var(--ink);
  }
  .series-line {
    position: absolute; left: 318px; top: 25px;
    writing-mode: vertical-rl; text-orientation: upright;
    font-size: 66px; font-weight: 900; letter-spacing: 6px; line-height: 1;
  }
  .author { position: absolute; left: 20px; top: 240px; width: 180px; text-align: center; }
  .author-label { color: var(--red); font-size: 18px; font-weight: 700; letter-spacing: 4px; line-height: 1.2; }
  .author-name { font-size: 40px; font-weight: 900; letter-spacing: 1px; line-height: 1.15; white-space: nowrap; }
  .author-roman { font-size: 15px; font-weight: 700; letter-spacing: 1px; margin-top: 4px; white-space: nowrap; }
  .title { margin: 0; }
  .title-column {
    position: absolute; top: 365px;
    font-family: "Noto Sans JP", sans-serif;
    font-size: 165px; font-weight: 900; line-height: 1;
    width: 210px; height: 400px;
    display: flex; justify-content: center; align-items: center;
  }
  .title-column span { writing-mode: vertical-rl; text-orientation: upright; letter-spacing: 8px; }
  .col-left { left: 10px; color: var(--red); }
  .col-center { left: 270px; color: var(--ink); }
  .col-right { left: 525px; color: var(--red); }
  .column-rule { position: absolute; top: 375px; width: 3px; height: 290px; background: var(--rule); }
  .rule-a { left: 235px; }
  .rule-b { left: 512px; }
  .edition {
    position: absolute; left: 0; top: 790px; width: 750px; text-align: center;
    font-size: 46px; font-weight: 900; letter-spacing: 2px; line-height: 1.2;
  }
  .promises { position: absolute; left: 25px; top: 932px; width: 700px; display: flex; justify-content: space-between; }
  .promise {
    width: 224px; height: 54px; box-sizing: border-box;
    border: 2.5px solid var(--ink); border-radius: 27px;
    display: flex; align-items: center; justify-content: center;
    font-family: "Noto Sans JP", sans-serif; font-size: 26px; font-weight: 900;
  }
  .promise em { font-style: normal; color: var(--red); }
  .catch-lead {
    position: absolute; left: 28px; top: 1028px;
    font-family: "Noto Sans JP", sans-serif; font-weight: 900; font-size: 38px; line-height: 1.45;
    white-space: nowrap;
  }
  .catch-lead em { font-style: normal; color: var(--red); font-size: 46px; }
  .catch-punch {
    position: absolute; left: 272px; top: 1018px;
    font-size: 100px; font-weight: 900; letter-spacing: -2px; line-height: 1.2; white-space: nowrap;
  }
</style>
</head>
<body>
<main class="cover">
  <div class="series-line">雑貨長者の</div>

  <div class="author">
    <div class="author-label">著者</div>
    <div class="author-name">早川蒼一</div>
    <div class="author-roman">SOICHI HAYAKAWA</div>
  </div>

  <h1 class="title">
    <div class="title-column col-right"><span>資金</span></div>
    <div class="title-column col-center"><span>調達</span></div>
    <div class="title-column col-left"><span>術</span></div>
  </h1>
  <div class="column-rule rule-a"></div>
  <div class="column-rule rule-b"></div>

  <div class="edition">〜開業ローン篇〜</div>

  <div class="promises">
    <div class="promise">会社を<em>つくる</em></div>
    <div class="promise">お金を<em>借りる</em></div>
    <div class="promise">原資が<em>できる</em></div>
  </div>

  <div class="catch-lead"><em>貯金</em>してから<br><em>起業</em>なんて</div>
  <div class="catch-punch">絶対ダメ!</div>
</main>
</body>
</html>
```